Business Card Design

We would like a business card that utilizes our current logo and keeps with the same feel - elegant and organic. Our farm isn't about mass production, it's about excellence, education, beautiful events and flowers - people, culture, and community.

Target Market(s)

Patrons to our farm who are interested in weddings, events, or our flowers and vegetables.

Contact Information for Business Card

Name, address, cell email (Danielle Hoskins, 2716 Wrenfield Rd, Larkmoor, CO 80642, cell 30.412.6638, email danielle@wrenfieldacres.com)

```html
<!DOCTYPE html>
<html lang="en">
<head>
<meta charset="utf-8">
<title>Wrenfield Acres – Business Card</title>
<link href="https://fonts.googleapis.com/css2?family=Cinzel:wght@500&family=Cabin:wght@400&display=swap" rel="stylesheet">
<style>
  :root {
    --backdrop: #242a29;
    --card: #e9e9e7;
    --sage: #5f7361;
    --bronze: #9a6b3a;
  }
  * { margin: 0; padding: 0; box-sizing: border-box; }
  html, body {
    width: 1200px; height: 800px; overflow: hidden;
    background: var(--backdrop);
  }
  .canvas {
    position: relative; width: 1200px; height: 800px;
    display: flex; align-items: center; justify-content: center; gap: 40px;
  }
  .card {
    position: relative; width: 530px; height: 303px;
    background: var(--card); border-radius: 22px; overflow: hidden;
  }
  /* Front */
  .top-band { position: absolute; top: 0; left: 0; right: 0; height: 10px; display: flex; }
  .top-band .sage { flex: 0 0 36%; background: var(--sage); height: 6px; }
  .top-band .bronze { flex: 1; background: var(--bronze); }
  .bottom-band { position: absolute; left: 0; right: 0; bottom: 0; height: 6px; background: var(--sage); }

  .brand-name {
    font-family: "Cinzel", serif; font-weight: 500; color: var(--sage);
    text-align: center; line-height: 1.15; letter-spacing: 0.04em;
  }
  .front .brand-name {
    position: absolute; left: 40px; top: 170px; width: 190px; font-size: 24px;
  }
  .brand-name .sub { display: block; font-size: 0.55em; letter-spacing: 0.45em; }

  .holder-name {
    position: absolute; left: 238px; top: 72px;
    font-family: "Cinzel", serif; font-weight: 500; font-size: 27px;
    color: var(--sage); letter-spacing: 0.02em; white-space: nowrap;
  }
  .contact-list {
    position: absolute; left: 240px; top: 122px; list-style: none;
    font-family: "Cabin", sans-serif; font-size: 13px; color: var(--bronze);
  }
  .contact-list li { display: flex; align-items: center; gap: 8px; margin-bottom: 10px; white-space: nowrap; }
  .contact-list svg { width: 15px; height: 15px; flex: none; }

  /* Back */
  .back { display: flex; align-items: center; justify-content: center; }
  .back .brand-name { font-size: 34px; }
</style>
</head>
<body>
<main class="canvas">
  <section class="card front" aria-label="Card front">
    <div class="top-band"><span class="sage"></span><span class="bronze"></span></div>
    <div class="brand-name">Wrenfield<span class="sub">Acres</span></div>
    <h1 class="holder-name">Danielle Hoskins</h1>
    <ul class="contact-list">
      <li>
        <svg viewBox="0 0 16 16" fill="none" stroke="currentColor" stroke-width="1.3"><path d="M8 15s5-5 5-8.5a5 5 0 0 0-10 0C3 10 8 15 8 15z"/><circle cx="8" cy="6.5" r="1.8"/></svg>
        2716 Wrenfield Rd, Larkmoor, CO 80642
      </li>
      <li>
        <svg viewBox="0 0 16 16" fill="none" stroke="currentColor" stroke-width="1.3"><circle cx="8" cy="8" r="6.3"/><path d="M5.8 5.2c.3-.4.8-.4 1 0l.6 1.2c.1.3 0 .6-.2.8l-.3.3c.4.9 1 1.5 1.9 1.9l.3-.3c.2-.2.5-.3.8-.2l1.2.6c.4.2.4.7 0 1-.6.6-1.5.8-2.3.4A6 6 0 0 1 5.4 7.5c-.4-.8-.2-1.7.4-2.3z"/></svg>
        30.412.6638
      </li>
      <li>
        <svg viewBox="0 0 16 16" fill="none" stroke="currentColor" stroke-width="1.3"><rect x="1.5" y="3.5" width="13" height="9" rx="1"/><path d="M1.8 4l6.2 5 6.2-5"/></svg>
        danielle@wrenfieldacres.com
      </li>
    </ul>
    <div class="bottom-band"></div>
  </section>

  <section class="card back" aria-label="Card back">
    <div class="brand-name">Wrenfield<span class="sub">Acres</span></div>
  </section>
</main>
</body>
</html>
```